Front book cover for a training course to help bakers get higher prices and sell more wedding cakes.

We need a front cover for a book that will be teaching bakers how to sell wedding cakes to get higher prices and book more orders. It is a business book. Do not make it look like we want brides to read it. Bakers will be judging the cover to see if it is worth their investment to read it. The title is already in the logo, so do not repeat it.

Target Market(s)

Bakers who sell wedding cakes

Industry/Entity Type

Bakery

Colors

Designer to choose colors to be used in the design.

Requirements
Must have
• Must use the logo. Must have author name: Lu Brandt. Must have subtitle: Boost Your Prices. Book More Brides. Build Your Empire.
Nice to have
• You are free to be creative. The concept is not to be pretty. It is a business sales and marketing book

```html
<!DOCTYPE html>
<html lang="en">
<head>
<meta charset="UTF-8">
<title>Tier Profit Pro – Front Cover</title>
<link href="https://fonts.googleapis.com/css2?family=Exo+2:wght@800&family=Sansita:wght@700&family=Bree+Serif&display=swap" rel="stylesheet">
<style>
  :root {
    --page-bg: #ffffff;
    --cover-bg: #f8f4ea;
    --ink-dark: #4a4b4f;
    --ink-black: #1c1c1c;
    --accent-pink: #ec4f7b;
    --cake-light: #f6ede2;
    --cake-mid: #e8d3bf;
    --cake-deep: #d4b49a;
  }
  * { margin: 0; padding: 0; box-sizing: border-box; }
  html, body {
    width: 1200px;
    height: 1200px;
    overflow: hidden;
    background: var(--page-bg);
  }
  .cover {
    position: absolute;
    left: 250px;
    top: 75px;
    width: 700px;
    height: 1050px;
    background: var(--cover-bg);
    box-shadow: 14px 18px 28px rgba(0, 0, 0, 0.35);
    overflow: hidden;
  }
  .brand {
    position: absolute;
    left: 0;
    top: 150px;
    width: 700px;
    display: flex;
    align-items: center;
    justify-content: center;
    gap: 18px;
  }
  .brand-dot {
    width: 38px;
    height: 38px;
    border-radius: 50%;
    background: var(--accent-pink);
    flex: none;
  }
  .brand-name {
    font-family: "Exo 2", sans-serif;
    font-weight: 800;
    font-size: 68px;
    line-height: 1;
    color: var(--ink-dark);
    letter-spacing: -0.5px;
    white-space: nowrap;
  }
  .cake-photo {
    position: absolute;
    left: 185px;
    top: 250px;
    width: 320px;
    height: 620px;
    border-radius: 40% 40% 18% 18% / 12% 12% 8% 8%;
    background: radial-gradient(ellipse at 50% 55%, var(--cake-light) 0%, var(--cake-mid) 60%, var(--cake-deep) 100%);
  }
  .connectors {
    position: absolute;
    left: 0;
    top: 0;
    width: 700px;
    height: 1050px;
  }
  .tagline {
    position: absolute;
    font-family: "Sansita", sans-serif;
    font-weight: 700;
    line-height: 1;
    white-space: nowrap;
  }
  .tagline-lead {
    color: var(--ink-dark);
    font-size: 38px;
  }
  .tagline-pill {
    background: var(--accent-pink);
    color: #ffffff;
    border-radius: 24px;
    padding: 5px 14px 7px;
    font-size: 36px;
  }
  .lead-prices { left: 60px; top: 400px; }
  .pill-prices { left: 55px; top: 443px; }
  .lead-brides { left: 478px; top: 412px; }
  .pill-brides { left: 468px; top: 449px; }
  .pill-empire {
    left: 350px;
    top: 886px;
    transform: translateX(-50%);
    font-size: 38px;
    border-radius: 28px;
    padding: 8px 20px 10px;
  }
  .author {
    position: absolute;
    left: 0;
    top: 995px;
    width: 700px;
    text-align: center;
    font-family: "Bree Serif", serif;
    font-size: 24px;
    letter-spacing: 4px;
    color: var(--ink-black);
    white-space: nowrap;
  }
</style>
</head>
<body>
  <main class="cover">
    <div class="brand">
      <span class="brand-dot"></span>
      <span class="brand-name">Tier Profit Pro</span>
    </div>

    <div class="cake-photo" role="img" aria-label="Photograph of a five-tier ivory wedding cake with lace bands and sugar flowers"></div>

    <svg class="connectors" viewBox="0 0 700 1050" aria-hidden="true">
      <path d="M 138 490 C 138 520, 137 600, 137 790 C 137 840, 180 878, 215 890" fill="none" stroke="var(--accent-pink)" stroke-width="1.6"/>
      <path d="M 553 494 C 553 520, 554 600, 554 770 C 554 830, 525 868, 485 890" fill="none" stroke="var(--accent-pink)" stroke-width="1.6"/>
    </svg>

    <span class="tagline tagline-lead lead-prices">Boost Your</span>
    <span class="tagline tagline-pill pill-prices">Prices.</span>
    <span class="tagline tagline-lead lead-brides">Book More</span>
    <span class="tagline tagline-pill pill-brides">Brides.</span>
    <span class="tagline tagline-pill pill-empire">Build Your Empire.</span>

    <p class="author">Author : Lu Brandt</p>
  </main>
</body>
</html>
```